Remedial massage therapist or clinical look

I would like a plain white or light colour background with front view of a musculoskeletal human body on the from on the left hand side, with Mirela Tostani remedial and sports massage therapist. On the back I want the back view of the musculoskeletal body on the left side with Mirela Tostani remedial and sports massage therapist, my contact details and appointment time and date. The colour of writing can be the same or close colour to the musculoskeletal body.
I don't want it to look to busy but also don't want it to be to plain,

Industry/Entity Type

Massage

Contact Information for Business Card

Mirela Tostani
Remedial and Sports Massage Therapist
Contact number: 0481536207
Email: tostanimirela41@quillmail.example

```html
<!DOCTYPE html>
<html lang="en">
<head>
<meta charset="utf-8">
<title>Mirela Tostani – Business Card</title>
<link rel="stylesheet" href="https://fonts.googleapis.com/css2?family=Arimo:wght@400;700&display=swap">
<style>
  :root {
    --page-bg: #ffffff;
    --page-edge: #8a8a8a;
    --card-edge: #555555;
    --ink-strong: #c2461f;
    --ink-soft: #e2805d;
    --muscle-light: #e8866a;
    --muscle-dark: #b8482c;
  }
  html, body {
    margin: 0;
    padding: 0;
    overflow: hidden;
    background: var(--page-bg);
  }
  .sheet {
    position: relative;
    width: 849px;
    height: 1200px;
    box-sizing: border-box;
    border: 1px solid var(--page-edge);
    background: var(--page-bg);
    font-family: "Arimo", Arial, sans-serif;
    overflow: hidden;
  }
  .card {
    position: absolute;
    left: 249px;
    width: 351px;
    height: 198px;
    box-sizing: border-box;
    border: 1px solid var(--card-edge);
    background: var(--page-bg);
  }
  .card--front { top: 373px; }
  .card--back { top: 628px; }
  .anatomy-figure {
    position: absolute;
    left: 21px;
    top: 15px;
    width: 68px;
    height: 167px;
    border-radius: 30px 30px 10px 10px;
    background: linear-gradient(180deg, var(--muscle-light), var(--muscle-dark));
  }
  .card-text {
    position: absolute;
    margin: 0;
    font-size: 13px;
    line-height: 15.5px;
  }
  .card--front .card-text { left: 142px; top: 76px; }
  .card--back .card-title { left: 113px; top: 32px; }
  .card--back .card-details { left: 113px; top: 88px; }
  .card-title {
    font-weight: 700;
    color: var(--ink-strong);
  }
  .card-details {
    font-weight: 400;
    color: var(--ink-soft);
  }
  .card-text span { display: block; }
</style>
</head>
<body>
<div class="sheet">
  <section class="card card--front">
    <div class="anatomy-figure" role="img" aria-label="Front view illustration of the human muscular system"></div>
    <p class="card-text card-title">
      <span>Mirela Tostani</span>
      <span>Remedial and Sports</span>
      <span>Massage Therapist</span>
    </p>
  </section>

  <section class="card card--back">
    <div class="anatomy-figure" role="img" aria-label="Back view illustration of the human muscular system"></div>
    <p class="card-text card-title">
      <span>Mirela Tostani</span>
      <span>Remedial and Sports Massage Therapist</span>
    </p>
    <p class="card-text card-details">
      <span>Contact number: 0481536207</span>
      <span>Email: tostanimirela41@quillmail.example</span>
      <span>Your appointment is at:</span>
      <span>Date</span>
      <span>Time</span>
    </p>
  </section>
</div>
</body>
</html>
```